Carpentry framing business card and logo design

We need a logo that works well with baseball caps, tee shirts and sweat shirts. We are a carpentry framing company specializing in apartment complexes and large residential communities. We work in what is known as the tri state area southeastern Pennsylvania , New Jersey and northern Delaware . We would like to see die signs using the old English letter M and royal blue colors. Also we stress WRSB compliance and safety.

Residential

Dalquist Construction Co Inc
1187 Harwick Lane
Ambler PA 19002
Rolf Dalquist
rolf1dalquist@quillmail.net
267-555-0148

```html
<!DOCTYPE html>
<html lang="en">
<head>
<meta charset="utf-8">
<title>Dalquist Construction Co Inc – Business Card</title>
<link rel="stylesheet" href="https://fonts.googleapis.com/css2?family=Tinos:wght@400;700&display=swap">
<style>
  :root {
    --backdrop: #2a1414;
    --card-white: #ffffff;
    --navy: #121a33;
    --navy-deep: #0d1326;
    --orange: #f28a1e;
    --text-light: #f2f2f2;
    --faint: #e9e9ec;
  }
  * { box-sizing: border-box; margin: 0; padding: 0; }
  html, body {
    width: 1200px;
    height: 800px;
    overflow: hidden;
    background: var(--backdrop);
  }
  .canvas {
    position: relative;
    width: 1200px;
    height: 800px;
    display: flex;
    align-items: center;
    justify-content: center;
  }
  .card {
    position: relative;
    width: 900px;
    height: 520px;
    background: var(--navy);
    font-family: "Tinos", "Times New Roman", serif;
    overflow: hidden;
    box-shadow: 0 20px 50px rgba(0,0,0,0.5);
  }
  .card__header {
    position: absolute;
    left: 0; top: 0;
    width: 100%;
    height: 225px;
    background: var(--card-white);
    display: flex;
    align-items: center;
    padding-left: 64px;
  }
  .card__stripe {
    position: absolute;
    left: 0; top: 225px;
    width: 100%;
    height: 14px;
    background: var(--orange);
  }
  .card__body {
    position: absolute;
    left: 0; top: 239px;
    width: 100%;
    bottom: 0;
    background: linear-gradient(180deg, var(--navy) 0%, var(--navy-deep) 100%);
    padding: 34px 0 0 64px;
  }
  .brand {
    display: flex;
    align-items: center;
    gap: 26px;
  }
  .brand__square {
    width: 120px;
    height: 120px;
    background: var(--navy);
    flex: none;
  }
  .brand__name {
    color: var(--navy);
    font-weight: 400;
    line-height: 1.05;
    letter-spacing: 1px;
    text-transform: uppercase;
  }
  .brand__name-main {
    display: block;
    font-size: 54px;
  }
  .brand__name-sub {
    display: block;
    font-size: 28px;
    letter-spacing: 2px;
  }
  .person {
    color: var(--orange);
    font-weight: 700;
    font-size: 38px;
    margin-bottom: 22px;
  }
  .contact-list {
    list-style: none;
    padding-left: 34px;
  }
  .contact-list__item {
    display: flex;
    align-items: center;
    gap: 10px;
    color: var(--text-light);
    font-size: 30px;
    line-height: 1.25;
  }
  .contact-list__icon {
    width: 26px;
    height: 26px;
    flex: none;
    fill: var(--orange);
  }
</style>
</head>
<body>
<main class="canvas">
  <article class="card">
    <header class="card__header">
      <div class="brand">
        <div class="brand__square"></div>
        <h1 class="brand__name">
          <span class="brand__name-main">Dalquist</span>
          <span class="brand__name-sub">Construction Co Inc</span>
        </h1>
      </div>
    </header>
    <div class="card__stripe"></div>
    <section class="card__body">
      <h2 class="person">Rolf Dalquist</h2>
      <ul class="contact-list">
        <li class="contact-list__item">
          <svg class="contact-list__icon" viewBox="0 0 24 24" aria-hidden="true">
            <path d="M6.6 10.8c1.4 2.8 3.8 5.1 6.6 6.6l2.2-2.2c.3-.3.7-.4 1-.2 1.1.4 2.3.6 3.6.6.6 0 1 .4 1 1V20c0 .6-.4 1-1 1C10.6 21 3 13.4 3 4c0-.6.4-1 1-1h3.5c.6 0 1 .4 1 1 0 1.3.2 2.5.6 3.6.1.3 0 .7-.2 1l-2.3 2.2z"/>
          </svg>
          <span>267-555-0148</span>
        </li>
        <li class="contact-list__item">
          <svg class="contact-list__icon" viewBox="0 0 24 24" aria-hidden="true">
            <path d="M2 5h20v14H2z M3.5 6.5 12 13l8.5-6.5" fill="none" stroke="#f28a1e" stroke-width="2" stroke-linejoin="round"/>
          </svg>
          <span>rolf1dalquist@quillmail.net</span>
        </li>
        <li class="contact-list__item">
          <svg class="contact-list__icon" viewBox="0 0 24 24" aria-hidden="true">
            <path d="M12 3 2 12h3v9h5v-6h4v6h5v-9h3z"/>
          </svg>
          <span>1187 Harwick Lane Ambler PA 19002</span>
        </li>
      </ul>
    </section>
  </article>
</main>
</body>
</html>
```